City department needs a bold and eye-catching poster design.

We need a poster to promote a survey targeting youth and young adults from 14-29 yr olds in the city of Strathcona County. We want poster designs that are bold, provocative and colourful. We want to poster to be a bright piece of art on the wall. See images attached. REQUIRED COPY: "Need something? We're listening" OR "Have Ideas? We're listening" OR "Your Wish? We're listening"

Target Market(s)

Youth, 14-29 yr olds

Industry/Entity Type

Government

Font styles to use
Sans Serif

Requirements
Must have
• REQUIRED COPY: Need something? We're listening"

```html
<!DOCTYPE html>
<html lang="en">
<head>
<meta charset="utf-8">
<title>Need Something? We're Listening — Youth Survey Poster</title>
<link rel="stylesheet" href="https://fonts.googleapis.com/css2?family=Saira+Extra+Condensed:wght@800&display=swap">
<style>
  :root {
    --page-bg: #e9e9e9;
    --frame-white: #ffffff;
    --wall-black: #121212;
    --paint-magenta: #c81a62;
    --paint-yellow: #f3e42d;
    --paint-blue: #5ca9e4;
    --paint-green: #4e9d46;
    --type-white: #ffffff;
    --type-blue: #5ca9e4;
    --type-red: #d8262e;
  }
  html, body {
    margin: 0;
    width: 1200px;
    height: 629px;
    overflow: hidden;
    background: var(--page-bg);
  }
  .canvas {
    position: relative;
    width: 1200px;
    height: 629px;
  }
  .poster {
    position: absolute;
    left: 366px;
    top: 12px;
    width: 468px;
    height: 605px;
    background: var(--frame-white);
    box-sizing: border-box;
    padding: 8px;
  }
  .poster-wall {
    position: relative;
    width: 100%;
    height: 100%;
    background: var(--wall-black);
    overflow: hidden;
  }
  .paint-bands,
  .headline {
    position: absolute;
    inset: 0;
    width: 100%;
    height: 100%;
  }
  .headline {
    margin: 0;
    overflow: hidden;
  }
  .headline-text {
    font-family: "Saira Extra Condensed", "Arial Narrow", sans-serif;
    font-weight: 800;
    text-transform: uppercase;
  }
  .headline-shadow-blue { fill: var(--type-blue); }
  .headline-shadow-red { fill: var(--type-red); }
  .headline-face {
    fill: var(--type-white);
    stroke: var(--wall-black);
    stroke-width: 1.2px;
    paint-order: stroke;
  }
</style>
</head>
<body>
<main class="canvas">
  <article class="poster">
    <div class="poster-wall" role="img" aria-label="Black painted brick wall with bright diagonal paint strokes">
      <svg class="paint-bands" viewBox="0 0 452 589" preserveAspectRatio="none" aria-hidden="true">
        <polygon class="band-magenta" fill="var(--paint-magenta)" points="0,0 205,0 0,185"/>
        <polygon class="band-yellow" fill="var(--paint-yellow)" points="268,0 405,0 452,38 452,235"/>
        <polygon class="band-blue" fill="var(--paint-blue)" points="0,380 210,589 0,589"/>
        <polygon class="band-green" fill="var(--paint-green)" points="452,400 452,589 245,589"/>
      </svg>
    </div>
    <svg class="headline" viewBox="0 0 452 589" role="heading" aria-level="1" aria-label="Need something? We're listening">
      <defs>
        <g id="headline-lines" class="headline-text" text-anchor="middle">
          <text x="226" y="222" font-size="170" textLength="325" lengthAdjust="spacingAndGlyphs">Need</text>
          <text x="226" y="292" font-size="80" textLength="325" lengthAdjust="spacingAndGlyphs">Something?</text>
          <text x="226" y="394" font-size="132" textLength="315" lengthAdjust="spacingAndGlyphs">We're</text>
          <text x="226" y="491" font-size="120" textLength="325" lengthAdjust="spacingAndGlyphs">Listening</text>
        </g>
      </defs>
      <use href="#headline-lines" class="headline-shadow-blue" transform="translate(-3 -2)"/>
      <use href="#headline-lines" class="headline-shadow-red" transform="translate(4 3)"/>
      <use href="#headline-lines" class="headline-face"/>
    </svg>
  </article>
</main>
</body>
</html>
```